Kestrel Summit 2019 Enemies of the End-Times Church Flyer

We want a church conference flyer designed. We are looking for a professional, yet catchy design that uses our brand colors and logo creatively while communicating key information of the event effectively. <br/>The flyer must include all of the following:<br/>Title: Kestrel Summit 2019<br/>Topic: The Enemies of The End-Times Church <br/>Subtitles: <br/> -How the antichrist raises an army by social behavior engineering. <br/>-How the architects of modern social constructs escaped the church's radar. <br/>-The Holy Spirit's end-times agenda:<br/> The Knock-Out Punch!<br/>Speaker: Prophet Marcus Toliver <br/>Dates/time: December 27, 28 & 29 at 6pm<br/>Location: Halvorn Community Center <br/> 241 Pellham Street <br/> Portland, ME 04102<br/>Contact info: phone: 207-555-0148 <br/>email: contact@brookmeadow.example <br/> www.vutel.example<br/>*The flyer must also include a picture of the speaker and our Vutel logo <br/>Thanks, we look forward to seeing what you come up with!

Colors

Designer to choose colors to be used in the design.

Requirements
Must have
• The flyer must include all of the following:
• Title: Kestrel Summit 2019
• Topic: The Enemies of The End-Times Church
• Subtitles:
• -How the antichrist raises an army by social behavior engineering.
• -How the architects of modern social constructs escaped the church's radar.
• -The Holy Spirit's end-times agenda:
• The Knock-Out Punch!
• Speaker: Prophet Marcus Toliver
• Dates/time: December 27, 28 & 29 at 6pm
• Location: Halvorn Community Center
• 241 Pellham Street
• Portland, ME 04102
• Contact info: phone: 207-555-0148
• email: contact@brookmeadow.example
• www.vutel.example
• *The flyer must also include a picture of the speaker and our Vutel logo
Should not have
• Pictures of crosses or church buildings

```html
<!DOCTYPE html>
<html lang="en">
<head>
<meta charset="utf-8">
<title>Kestrel Summit 2019</title>
<link rel="stylesheet" href="https://fonts.googleapis.com/css2?family=Montserrat:wght@500;600&family=Open+Sans:ital,wght@0,400;0,600;0,700;1,700&display=swap">
<style>
  :root {
    --paper: #f1f1f1;
    --navy: #0f3a5f;
    --ink: #1c2a38;
    --sky: #7fd3ea;
    --white: #ffffff;
    --photo-dark: #3a3236;
    --photo-light: #b9b4ae;
  }
  * { margin: 0; padding: 0; box-sizing: border-box; }
  html, body { width: 928px; height: 1200px; overflow: hidden; background: var(--paper); }
  .flyer {
    position: relative; width: 928px; height: 1200px; overflow: hidden;
    background: var(--paper); font-family: "Open Sans", Arial, sans-serif; color: var(--navy);
  }
  .corner-block { position: absolute; left: 0; top: 0; width: 171px; height: 85px; background: var(--navy); }
  .speaker-photo {
    position: absolute; left: 104px; top: 0; width: 721px; height: 542px;
    background: radial-gradient(ellipse at 45% 45%, #6b5a55 0%, var(--photo-dark) 45%, transparent 70%),
                linear-gradient(180deg, var(--photo-light) 0%, #8d8780 55%, #6e6862 100%);
  }
  .speaker-tag {
    position: absolute; left: 596px; top: 327px; width: 332px; height: 85px;
    background: var(--sky); padding: 14px 0 0 14px;
  }
  .speaker-name { font-weight: 700; font-size: 21px; letter-spacing: 0.2px; color: var(--navy); }
  .speaker-role { font-size: 20px; color: var(--navy); text-align: right; padding-right: 46px; line-height: 1.3; }
  .title-ring { position: absolute; left: 220px; top: 438px; }
  .event-title {
    position: absolute; left: 224px; width: 478px; text-align: center;
    font-family: "Montserrat", Arial, sans-serif; color: var(--navy);
  }
  .event-title .main { position: absolute; top: 598px; left: 0; right: 0; font-size: 74px; font-weight: 600; letter-spacing: 3px; line-height: 1; }
  .event-title .sub { position: absolute; top: 687px; left: 0; right: 0; font-size: 26px; font-weight: 500; letter-spacing: 3.5px; line-height: 1; }
  .event-dates {
    position: absolute; top: 764px; left: 224px; width: 478px; text-align: center;
    font-family: "Montserrat", Arial, sans-serif; font-weight: 500; font-size: 19px; line-height: 28px; color: var(--ink);
  }
  .topic { position: absolute; right: 30px; top: 964px; text-align: right; }
  .topic h2 { font-size: 21px; font-weight: 600; letter-spacing: 0.6px; color: var(--navy); margin-bottom: 12px; margin-right: -2px; }
  .topic li { list-style: none; font-style: italic; font-weight: 700; font-size: 16px; line-height: 29px; color: var(--ink); }
  .brand-box {
    position: absolute; left: 42px; top: 987px; width: 148px; height: 165px; background: var(--white);
    display: flex; align-items: center; justify-content: center; gap: 6px;
  }
  .brand-dot { width: 10px; height: 10px; border-radius: 50%; background: var(--navy); }
  .brand-name { font-family: "Open Sans", Arial, sans-serif; font-weight: 600; font-size: 26px; letter-spacing: 1px; color: var(--navy); }
  .venue {
    position: absolute; left: 283px; top: 1127px; width: 330px; text-align: center;
    font-size: 14.5px; line-height: 19px; color: var(--ink);
  }
  .contact { position: absolute; left: 683px; top: 1083px; font-size: 14.5px; line-height: 19px; color: var(--ink); }
</style>
</head>
<body>
<main class="flyer">
  <div class="corner-block"></div>
  <div class="speaker-photo" role="img" aria-label="Portrait of the speaker, Prophet Marcus Toliver, in front of bookshelves"></div>
  <div class="speaker-tag">
    <p class="speaker-name">PROPHET MARCUS TOLIVER</p>
    <p class="speaker-role">speaker</p>
  </div>

  <svg class="title-ring" width="486" height="486" viewBox="0 0 486 486" aria-hidden="true">
    <circle cx="243" cy="243" r="239" fill="none" stroke="var(--navy)" stroke-width="4"/>
  </svg>
  <h1 class="event-title">
    <span class="main">KESTREL</span>
    <span class="sub">SUMMIT 2019</span>
  </h1>
  <p class="event-dates">DEC. 27,28 &amp; 29, 2019<br>6 PM</p>

  <section class="topic">
    <h2>THE ENEMIES of the&nbsp; END-TIMES CHURCH</h2>
    <ul>
      <li>How the antichrist raises an army by social behavior engineering.</li>
      <li>How the architects of modern social constructs escaped the church’s radar</li>
      <li>The Holy Spirit’s end-times agenda: The Knock-Out Punch!</li>
    </ul>
  </section>

  <div class="brand-box">
    <span class="brand-dot"></span>
    <span class="brand-name">VUTEL</span>
  </div>

  <address class="venue" style="font-style:normal">Halvorn Community Center<br>241 Pellham Street Portland, ME 04102</address>
  <address class="contact" style="font-style:normal">Contact: 207-555-0148<br>contact@brookmeadow.example<br>www.vutel.example</address>
</main>
</body>
</html>
```